Logo and business card for optometric practice
Curtis Hallorann & Associates
Marta Pelovska, O.D.
Oscar Tremwitz, O.D.
Neil Borromi, O.D.
417 Pembrook Parkway
Ashford Hollow, Oregon 97204
555-902-4471

Target Market(s)

Patients, general public

Industry/Entity Type

Business

Logo Text

Curtis Hallorann & Associates Optometrists

Logo styles of interest
Pictorial/Combination Logo
Font styles to use
Serif
Sans Serif

Requirements
Must have
• current inspiration: realistic or photo closeup of eye, with interesting treatment of the iris OR
tech look, with closeup of eye and grid like the doctor is looking through a camera or microscope to view the eye up close
Should not have
• NO cartoons

```html
<!DOCTYPE html>
<html lang="en">
<head>
<meta charset="utf-8">
<title>Curtis Hallorann &amp; Associates — Business Card</title>
<link rel="stylesheet" href="https://fonts.googleapis.com/css2?family=Raleway:wght@300;400&display=swap">
<style>
  :root {
    --ink: #12252a;
    --gold: #c9973f;
    --paper: #ffffff;
  }
  * { margin: 0; padding: 0; box-sizing: border-box; }
  html, body {
    width: 1200px;
    height: 329px;
    overflow: hidden;
    background: var(--paper);
    font-family: "Raleway", Arial, sans-serif;
  }
  .card-set {
    position: relative;
    width: 1200px;
    height: 329px;
  }

  /* Front of card */
  .card-front {
    position: absolute;
    left: 0; top: 0;
    width: 575px;
    height: 329px;
    background: var(--ink);
    color: var(--gold);
    text-align: center;
  }
  .card-front .brand-dot {
    position: absolute;
    left: 286px; top: 103px;
    width: 19px; height: 19px;
    border-radius: 50%;
    background: var(--gold);
  }
  .card-front .brand-name {
    position: absolute;
    left: 0; right: 0;
    top: 178px;
    font-size: 34px;
    font-weight: 300;
    letter-spacing: 0.2px;
    white-space: nowrap;
  }
  .card-front .brand-tagline {
    position: absolute;
    left: 0; right: 0;
    top: 225px;
    font-size: 22px;
    font-weight: 300;
  }

  /* Back of card */
  .card-back {
    position: absolute;
    left: 577px; top: 0;
    width: 623px;
    height: 329px;
    background: var(--paper);
    color: var(--ink);
  }
  .card-back .brand-mark {
    position: absolute;
    left: 0; right: 0;
    top: 42px;
    text-align: center;
    font-size: 16px;
    font-weight: 300;
    color: var(--gold);
  }
  .card-back .doctor-name {
    position: absolute;
    left: 0; right: 0;
    top: 119px;
    text-align: center;
    font-size: 28px;
    font-weight: 400;
    padding-left: 26px;
    white-space: nowrap;
  }
  .card-back .address {
    position: absolute;
    left: 49px;
    top: 227px;
    font-size: 20px;
    font-weight: 400;
    line-height: 26px;
    font-style: normal;
    white-space: nowrap;
  }
  .card-back .phone {
    position: absolute;
    right: 3px;
    top: 253px;
    font-size: 20px;
    font-weight: 400;
    line-height: 26px;
    white-space: nowrap;
  }
  .card-back .footer-band {
    position: absolute;
    left: 47px; right: 0;
    top: 294px;
    height: 35px;
    background: var(--ink);
  }
</style>
</head>
<body>
  <main class="card-set">
    <section class="card-front">
      <span class="brand-dot" aria-hidden="true"></span>
      <h1 class="brand-name">Curtis Hallorann &amp; Associates</h1>
      <p class="brand-tagline">Optometric practice</p>
    </section>

    <section class="card-back">
      <p class="brand-mark">Curtis Hallorann &amp; Associates</p>
      <h2 class="doctor-name">Marta Pelovska, O.D.</h2>
      <address class="address">417 Pembrook Parkway<br>Ashford Hollow, Oregon 97204</address>
      <p class="phone">555-902-4471</p>
      <div class="footer-band"></div>
    </section>
  </main>
</body>
</html>
```